Massage Therapy and Personal Training Business Card (Lorvex Wellness)

I need a logo design based in Washington. The company is called Lorvex Wellness. Lorvex are my initials. I specialize in massage therapy and personal training and general wellness of my clients. I've tried getting designs but haven't quite yet found what I'm looking for. I'm not inclined to a certain color yet but some color that resembles wellness such as light blue and white or green and white. Again, I'm not really picky about that. Thank you in advance

Industry/Entity Type

Business

Contact Information for Business Card

Have the description on one side and space for writing information on the back side such as number, appt, etc. I have an example attached. I see a lot of these card. I dont want the exact one, but something similar. Simple, professional and elegant.

Colors

Designer to choose colors to be used in the design.

Requirements
Must have
• Space on the back side to write
• A professional, elegant look
Should not have
• cartoon like style.

```html
<!DOCTYPE html>
<html lang="en">
<head>
<meta charset="utf-8">
<title>Lorvex Wellness Business Card</title>
<link rel="stylesheet" href="https://fonts.googleapis.com/css2?family=Open+Sans:wght@400;700&family=Questrial&display=swap">
<style>
  :root {
    --stage: #ecebe8;
    --card-dark: #383838;
    --card-light: #ffffff;
    --ink-light: #ffffff;
    --ink-dark: #2a2a2a;
    --leaf-green: #9dca3b;
    --write-line: #8a8a8a;
  }
  * { margin: 0; padding: 0; box-sizing: border-box; }
  html, body { width: 1200px; height: 900px; overflow: hidden; }
  body { background: var(--stage); position: relative; font-family: "Open Sans", Arial, sans-serif; }

  .card { position: absolute; box-shadow: 0 6px 18px rgba(0,0,0,.18); }

  .card-front { left: 78px; top: 34px; width: 587px; height: 364px; background: var(--card-dark); color: var(--ink-light); }
  .holder-name { position: absolute; left: 30px; top: 45px; font-size: 19px; font-weight: 700; letter-spacing: .3px; }
  .holder-title { position: absolute; left: 30px; top: 69px; font-size: 15.5px; }
  .contact-list { position: absolute; left: 30px; top: 207px; list-style: none; font-size: 15.5px; line-height: 21.5px; }
  .contact-list li { display: flex; align-items: center; gap: 8px; }
  .contact-list svg { width: 12px; height: 12px; fill: var(--ink-light); flex: none; }
  .address { position: absolute; left: 30px; top: 280px; font-size: 15.5px; line-height: 22px; }
  .brand-mark { position: absolute; left: 355px; top: 95px; width: 130px; height: 130px; border-radius: 50%; background: var(--leaf-green); }
  .brand-name-front { position: absolute; left: 320px; top: 250px; width: 200px; text-align: center; font-family: "Questrial", Arial, sans-serif; font-size: 24px; color: var(--ink-light); }

  .card-back { left: 388px; top: 505px; width: 566px; height: 352px; background: var(--card-light); }
  .brand-lockup { position: absolute; left: 0; top: 138px; width: 100%; display: flex; justify-content: center; align-items: center; gap: 12px; }
  .brand-name-back { font-family: "Questrial", Arial, sans-serif; font-size: 44px; color: var(--ink-dark); line-height: 1; }
  .brand-dot { width: 22px; height: 22px; border-radius: 50%; background: var(--leaf-green); }
  .write-lines { position: absolute; left: 119px; top: 229px; width: 329px; }
  .write-lines span { display: block; height: 1.5px; background: var(--write-line); margin-bottom: 40.5px; }
</style>
</head>
<body>
  <section class="card card-front">
    <h1 class="holder-name">DANIEL MARSH</h1>
    <p class="holder-title">Managing Director</p>
    <ul class="contact-list">
      <li><svg viewBox="0 0 24 24"><path d="M6.6 10.8a15 15 0 0 0 6.6 6.6l2.2-2.2a1 1 0 0 1 1-.25 11.4 11.4 0 0 0 3.6.57 1 1 0 0 1 1 1V20a1 1 0 0 1-1 1A17 17 0 0 1 3 4a1 1 0 0 1 1-1h3.5a1 1 0 0 1 1 1c0 1.25.2 2.45.57 3.57a1 1 0 0 1-.25 1z"/></svg>(044)987654321</li>
      <li><svg viewBox="0 0 24 24"><path d="M2 5h20v14H2z M3.5 6.5 12 13l8.5-6.5" stroke="#383838" stroke-width="1.6"/></svg>hello@lorvexmail.com</li>
      <li><svg viewBox="0 0 24 24"><circle cx="12" cy="12" r="10"/><path d="M2 12h20M12 2c3 3 3 17 0 20M12 2c-3 3-3 17 0 20" stroke="#383838" stroke-width="1.5" fill="none"/></svg>www.lorvexwellness.com</li>
    </ul>
    <p class="address">5678, Harbor Lane Way,<br>Country name, 67890</p>
    <div class="brand-mark"></div>
    <p class="brand-name-front">Lorvex Wellness</p>
  </section>

  <section class="card card-back">
    <div class="brand-lockup">
      <span class="brand-name-back">Lorvex Wellness</span>
      <span class="brand-dot"></span>
    </div>
    <div class="write-lines"><span></span><span></span><span></span></div>
  </section>
</body>
</html>
```